Premium Personal Brand — Facebook Banner (Used Across All Platforms)

Update — Additional Color Direction
In addition to the dark charcoal/slate direction already described, I'm also interested in seeing variants with:
Dark navy blue — Deep, authoritative, intelligence-community feel. Same textured/matte treatment, not flat or bright.
Warm charcoal with steel blue accent — Keep the dark base but introduce a subtle steel blue gradient, accent line, or tonal shift. Sophisticated, modern, adds dimension without adding color noise.
Both should maintain the same premium, restrained, architectural feel described in the original brief. No bright blues, no corporate PowerPoint energy — think midnight, think depth, think weight.
Everything else in the brief remains the same.
I am building a premium personal brand as an executive advisor to founders ($5M+ revenue).
This contest is Facebook-banner–focused, but the design must represent a visual system that will be reused across:
- LinkedIn
- YouTube
I- nstagram
- X (Twitter)
- Website hero sections and other brand touchpoints
Think of the Facebook banner as the primary expression of the brand — not a one-off graphic.
This project is about discovering a high-end visual style and brand feel, not decoration.
What to design
Please submit one cohesive visual system, shown primarily as:
- Facebook banner (primary focus)
The same design language should clearly translate to all platforms listed above.
Designers are responsible for using the current recommended dimensions for each platform.
Quick clarification on background direction:
Backgrounds should have depth and texture, not flat color fields. Avoid pure white, light grey, or solid black backgrounds. Think matte, architectural materials — stone, graphite, concrete, steel — not blank canvases. Subtle tonal variation is encouraged. Obvious gradients or decorative patterns are not.
Text to use
Primary Headline:
- Your Business Is Too Valuable To Be Run On Hope.
Subheadline:
- You didn’t build a business to become its prisoner.
Name:
Paul Whitaker
The headline should be the dominant visual element.
Logo note (important)
My personal logo is currently being finalized.
For this contest:
- Use a simple “PW” monogram placeholder
- Clean, bold, geometric sans-serif
- Do not design a logo
- The winning design must allow an easy logo swap later.
Headshot note (important)
- Please do not include a headshot in the banner design.
- Most platforms display a circular profile image separately.
- The banner should stand on its own using typography, layout, and tone only.
- Design the banner assuming the profile photo will sit nearby, not inside the banner.
Style direction
The design should feel:
- Premium
- Calm
- Confident
- Restrained
- High-trust
- Dark, neutral backgrounds are preferred.
- Fewer elements are better than more.
Think:
- Owner-level advisor
- Private equity / boardroom tone
- Industrial, Modern, Minimalist, Elite, Architectural, not decorative
What to avoid
Please do not submit designs that feel:
- Promotional, hype-driven, or salesy
- Like a coach, guru, or agency
- Bright, colorful, or gradient-heavy
- Busy or over-designed
- Based on stock photos
- No motivational speaker energy.
Reaction test
- If someone sees this banner on Facebook (or later on LinkedIn, YouTube, etc.), the reaction should be:
“That person is serious. I’d trust them with important decisions.”
Final note
- I am not looking for many variations.
- I am looking for one strong visual direction you believe in.
Simple beats clever.
- Restraint beats decoration.

```html
<!DOCTYPE html>
<html lang="en">
<head>
<meta charset="UTF-8">
<title>Paul Whitaker — Facebook Cover Concept</title>
<link rel="stylesheet" href="https://fonts.googleapis.com/css2?family=Montserrat:wght@400;700;800&display=swap">
<style>
  :root {
    --page: #ffffff;
    --navy-deep: #0a2f58;
    --navy-mid: #0e3f70;
    --navy-soft: #134a7e;
    --accent: #2a9fe2;
    --headline-light: #d6dee7;
    --sub-text: #e6ebf1;
    --rule: rgba(255, 255, 255, 0.22);
    --corner-tone: rgba(150, 176, 206, 0.38);
    --caption: #333333;
  }
  * { margin: 0; padding: 0; box-sizing: border-box; }
  html, body {
    width: 1200px;
    height: 572px;
    overflow: hidden;
    background: var(--page);
    font-family: "Montserrat", Arial, sans-serif;
  }
  .board { position: relative; width: 1200px; height: 572px; }

  .cover {
    position: absolute;
    left: 92px;
    top: 92px;
    width: 1029px;
    height: 392px;
    overflow: hidden;
  }
  .cover-texture {
    position: absolute;
    inset: 0;
    background:
      radial-gradient(ellipse 65% 75% at 50% 35%, var(--navy-soft) 0%, transparent 75%),
      linear-gradient(160deg, var(--navy-mid) 0%, #0d3b69 50%, var(--navy-deep) 100%);
  }
  .corner-accent { position: absolute; }
  .corner-accent--top-left {
    left: 0; top: 0; width: 139px; height: 185px;
    background: radial-gradient(ellipse 100% 100% at 0% 0%, var(--corner-tone) 0%, transparent 75%);
  }
  .corner-accent--bottom-right {
    right: 0; bottom: 0; width: 193px; height: 225px;
    background: radial-gradient(ellipse 100% 100% at 100% 100%, var(--corner-tone) 0%, transparent 75%);
  }

  .monogram {
    position: absolute;
    left: 232px;
    top: 51px;
    font-weight: 800;
    font-size: 100px;
    line-height: 100px;
    letter-spacing: -2px;
    color: var(--accent);
  }

  .message { position: absolute; left: 434px; top: 47px; width: 560px; }
  .headline { font-weight: 400; text-transform: uppercase; color: var(--headline-light); }
  .headline-line {
    display: block;
    font-size: 42px;
    line-height: 46px;
    letter-spacing: -1px;
    white-space: nowrap;
  }
  .headline-line--first { font-size: 34px; letter-spacing: -0.5px; }
  .headline-strong { font-weight: 800; color: var(--accent); }

  .divider {
    width: 411px;
    height: 1px;
    margin: 6px 0 6px;
    background: var(--rule);
  }
  .subheadline {
    font-weight: 400;
    font-size: 27px;
    line-height: 36px;
    letter-spacing: -0.3px;
    color: var(--sub-text);
  }
  .signature {
    margin-top: 25px;
    font-weight: 700;
    font-size: 28px;
    line-height: 34px;
    text-transform: uppercase;
    color: var(--accent);
  }

  .caption {
    position: absolute;
    left: 0;
    top: 513px;
    width: 1200px;
    text-align: center;
    font-weight: 400;
    font-size: 19px;
    color: var(--caption);
  }
</style>
</head>
<body>
<main class="board">
  <section class="cover" aria-label="Facebook cover">
    <div class="cover-texture" role="img" aria-label="Dark navy matte concrete texture"></div>
    <div class="corner-accent corner-accent--top-left" role="img" aria-label="Angular translucent facet decoration"></div>
    <div class="corner-accent corner-accent--bottom-right" role="img" aria-label="Angular translucent facet decoration"></div>

    <div class="monogram">PW</div>

    <div class="message">
      <h1 class="headline">
        <span class="headline-line headline-line--first">Your business is</span>
        <span class="headline-line">Too <span class="headline-strong">Valuable</span></span>
        <span class="headline-line">To be <span class="headline-strong">Run on hope.</span></span>
      </h1>
      <div class="divider"></div>
      <p class="subheadline">You didn’t build a business<br>to become its prisoner.</p>
      <p class="signature">Paul Whitaker</p>
    </div>
  </section>

  <p class="caption">Design Concept PW FB Cover -01</p>
</main>
</body>
</html>
```